Trifold brochure for Thai yoga massage practice (In a Combat gym and a Spa)

I am a Practitioner of Thai massage in Toronto, and will in the near future be offering personal training with transitional fitness from couch potato to weekend warriors.

I train in Muay-thai and my current stream of clients are "thai tigers" in need of restorative therapy to get them back on their feet - hence the website name Ravenhush.com.
My other stream of clients are in a Lovely Spa on a rooftop patio (if you're ever in Toronto come on by).

So I have the best of two worlds (injuries vs. pure bliss) Dark vs. Light

I want to introduce Thai yoga massage to a new modern audience. Thai massage is an ancient, effective hybrid therapy incorporating traditional acupressure/ body meridian therapy and human kinetics simultaneously.

Brochures are meant for distribution to martial arts studios, fitness gyms and other spas.

I am open to eye-catching, out of the box ideas.

My website: www.ravenhush.com (I am in the process of editing this new web space - apologies for the very basic nature of it)

Pictures are attached for review or view my link:
https://files.pelorandrop.net/share?id=7Xq41mPbR2kLwZt9VhDs&ref=open

Thank you!

Target Market(s)

20-45 year old fitness enthusiast for a gym audience
or 20-55 year old looking for general wellness/ relaxation
or combination of both (yin/yang type design)

Industry/Entity Type

Training

Font styles to use
Decorative

Requirements
Must have
• Will be looking for innovation, clever, witty design, please be creative. Toronto is a quirky city, I welcome quirky, yet tasteful designs.

Please use a good amount of flow, and streaming lines.
Nice to have
• If we could have a yin / yang effect that would be nice (Combat restoration vs. Relaxation)
Should not have
• Please do not have text / designs that convey the stereotypical nonsense that surround Asian based massage (my cup is full already).

```html
<!DOCTYPE html>
<html lang="en">
<head>
<meta charset="utf-8">
<title>Thai Yoga Massage – Trifold Brochure</title>
<link rel="stylesheet" href="https://fonts.googleapis.com/css2?family=Mulish:wght@400;600;700&family=Varela+Round&display=swap">
<style>
  :root {
    --stage: #c9ccce;
    --paper: #dcd6cc;
    --teal: #1f7f8c;
    --teal-deep: #0f3c46;
    --coral: #ef7a5e;
    --ink: #3a3632;
    --white: #ffffff;
    --photo-warm: #8a6a52;
    --photo-mat: #5a4f7a;
  }
  * { box-sizing: border-box; margin: 0; padding: 0; }
  html, body { width: 1200px; height: 800px; overflow: hidden; background: var(--stage); }
  .brochure {
    position: relative; width: 1200px; height: 800px;
    background: var(--paper); overflow: hidden;
    font-family: "Mulish", Arial, sans-serif; color: var(--ink);
  }
  .fold { position: absolute; top: 0; bottom: 0; width: 1px; background: rgba(0,0,0,.08); }
  .fold--one { left: 400px; } .fold--two { left: 800px; }
  .stripe-band { position: absolute; inset: 0; width: 1200px; height: 800px; pointer-events: none; }

  .photo { position: absolute; }
  .photo--portrait {
    left: 20px; top: 215px; width: 360px; height: 170px;
    background: linear-gradient(135deg, #6f6a62, #a79c8e 55%, #4e5552);
  }
  .photo--still-life {
    left: 420px; top: 135px; width: 200px; height: 120px;
    background: linear-gradient(120deg, #5a3a2e, #b9a98a 50%, #d8dcc8);
  }
  .photo--pose {
    left: 1060px; width: 130px; height: 100px;
    background: linear-gradient(160deg, #2c2a2e, var(--photo-warm) 45%, var(--photo-mat));
  }
  .photo--pose-1 { top: 20px; } .photo--pose-2 { top: 135px; }
  .photo--pose-3 { top: 250px; } .photo--pose-4 { top: 365px; }

  .hook {
    position: absolute; left: 20px; top: 396px; width: 360px;
    font-family: "Varela Round", "Mulish", sans-serif;
    color: var(--teal); font-size: 16px; line-height: 1.25; text-align: center; font-weight: 700;
  }
  .section-title {
    font-family: "Varela Round", "Mulish", sans-serif;
    color: var(--teal); font-weight: 400; letter-spacing: .5px; text-transform: uppercase;
  }
  .intro { position: absolute; left: 30px; top: 612px; width: 345px; }
  .intro .section-title { font-size: 24px; margin-bottom: 6px; }
  .intro p { font-size: 13px; line-height: 1.4; }

  .practice { position: absolute; left: 430px; top: 270px; width: 345px; }
  .practice .section-title { font-size: 24px; margin-bottom: 8px; }
  .practice p { font-size: 13px; line-height: 1.45; margin-bottom: 4px; }

  .benefits { position: absolute; left: 830px; top: 40px; width: 215px; }
  .benefits .section-title { font-size: 19px; line-height: 1.25; margin-bottom: 18px; }
  .benefits ul { list-style: none; }
  .benefits li { font-size: 14px; line-height: 1.3; margin-bottom: 11px; padding-left: 14px; position: relative; }
  .benefits li::before { content: "•"; position: absolute; left: 0; color: var(--ink); }
</style>
</head>
<body>
<main class="brochure">
  <svg class="stripe-band" viewBox="0 0 1200 800">
    <defs>
      <linearGradient id="stripeTone" x1="0" y1="0" x2="1" y2="1">
        <stop offset="0" stop-color="#1d7f8e"/>
        <stop offset=".5" stop-color="#0f3c46"/>
        <stop offset="1" stop-color="#1d7f8e"/>
      </linearGradient>
    </defs>
    <path role="img" aria-label="Teal and black tiger-stripe pattern band"
      d="M0 0 H840 C 790 70 720 115 600 120 C 430 128 260 150 0 200 Z" fill="url(#stripeTone)"/>
    <path d="M0 200 C 260 150 430 128 600 120 C 720 115 790 70 840 0 H860 C 805 85 730 130 610 137 C 440 146 270 168 0 215 Z" fill="var(--white)"/>
    <path d="M400 800 V745 C 520 740 640 705 780 640 L800 632 V800 Z" fill="var(--coral)"/>
    <path d="M400 745 C 520 740 640 705 780 640 L800 632" stroke="var(--teal)" stroke-width="5" fill="none"/>
    <path d="M800 632 C 900 600 1000 560 1200 545 V520 C 1010 530 900 575 800 610 Z" fill="var(--coral)"/>
    <path d="M800 632 C 900 600 1000 560 1200 545" stroke="var(--teal)" stroke-width="4" fill="none"/>
  </svg>

  <div class="fold fold--one"></div>
  <div class="fold fold--two"></div>

  <!-- Left panel -->
  <div class="photo photo--portrait" role="img" aria-label="Portrait photo of the practitioner in a studio"></div>
  <p class="hook">To all fellow weekend warriors, desk jockeys, and training addicts...to all my TIGERS:<br>
    Have we not felt the pain for the gain?<br>
    Ache in the sake of the sport?<br>
    Pushed hard for that push back to know our strength?<br>
    Worked 12 hour shifts at a desk to feel your back breaking??<br>
    I have. Let me help you.</p>
  <section class="intro">
    <h2 class="section-title">Introduction</h2>
    <p>My name is Mara Lindqvist and I am a Holistic Practitioner of Thai Yoga Massage based in the Beaches area in eastern Toronto. For my practice I am especially interested in the incorporation of Thai Yoga massage in assisted recovery for Sport specific injuries as well as repetitive stress syndrome from work or play.</p>
  </section>

  <!-- Middle panel -->
  <div class="photo photo--still-life" role="img" aria-label="Photo of herbal compresses and spa items"></div>
  <section class="practice">
    <h2 class="section-title">Thai Yoga Massage</h2>
    <p>This form of bodywork therapy is 2500 years in the making and is practiced and regulated in Thailand today. With many different lineages and styles the concept of Thai Yoga Massage is the same.</p>
    <p>A session is commenced traditionally on a padded floor or mat with the client clothed in comfortable garments that allow freedom of movement.</p>
    <p>Through the placement of the client's body in a series of yoga like poses a trained practitioner is able to establish levels of structural balance. A combination of rhythmic techniques with specific poses allows the practitioner to stimulate the Sen (synonymous with energy lines or meridians), isolate and release trigger points in a client.</p>
  </section>

  <!-- Right panel -->
  <section class="benefits">
    <h2 class="section-title">Benefits of Thai Yoga Massage:</h2>
    <ul>
      <li>Pain relief</li>
      <li>Release muscular tension</li>
      <li>Stress relief</li>
      <li>Promotes structural balance</li>
      <li>Improves posture</li>
      <li>Enhances circulation</li>
      <li>Supports healing</li>
      <li>Improves flexibility</li>
      <li>Regulates nervous energy</li>
      <li>Encourages better breathing</li>
    </ul>
  </section>
  <div class="photo photo--pose photo--pose-1" role="img" aria-label="Photo of a Thai yoga massage stretch on a mat"></div>
  <div class="photo photo--pose photo--pose-2" role="img" aria-label="Photo of a seated assisted stretch"></div>
  <div class="photo photo--pose photo--pose-3" role="img" aria-label="Photo of a leg compression technique"></div>
  <div class="photo photo--pose photo--pose-4" role="img" aria-label="Photo of a back stretch on the mat"></div>
</main>
</body>
</html>
```